Help me make landing pages for my web application that are mobile friendly

I need to make 2 mobile friendly landing pages for an application. The 2 pages will be related. First I need a home page and then I need a working page. I do not want to change the color scheme or logos. Just layout and design.

```html
<!DOCTYPE html>
<html lang="en">
<head>
<meta charset="utf-8">
<title>ShiftCover – Mobile Screens</title>
<link href="https://fonts.googleapis.com/css2?family=Roboto:wght@400;500;700&display=swap" rel="stylesheet">
<style>
:root{
  --teal:#2aa8d0;
  --purple:#6a4fa3;
  --grad:linear-gradient(90deg,#2aa8d0 0%,#3b93c9 45%,#6a4fa3 100%);
  --ink:#1d1d1f;
  --muted:#5d5f66;
  --green:#4a9a2e;
  --red:#e0201b;
  --stage:#333132;
  --line:#dfe6ee;
  --font:'Roboto',Arial,sans-serif;
}
*{box-sizing:border-box;margin:0;padding:0}
html,body{width:1015px;height:1200px;overflow:hidden;background:var(--stage);font-family:var(--font)}
.stage{position:absolute;left:0;top:0;width:1532px;height:1812px;transform:scale(0.66254);transform-origin:0 0;
  background:radial-gradient(ellipse at 50% 40%,#3a3839 0%,#2f2d2e 80%)}
.screen{position:absolute;top:81px;width:414px;background:#fff;overflow:hidden}
.screen--list{left:81px;height:1344px}
.screen--menu{left:559px;height:1344px}
.screen--detail{left:1037px;height:1651px}
.header{position:absolute;left:0;top:0;width:414px;height:240px}
.icon-btn{position:absolute;top:19px;width:40px;height:40px;border-radius:50%;background:#fff;display:flex;align-items:center;justify-content:center}
.brand{position:absolute;left:110px;top:20px;height:38px;display:flex;align-items:center;gap:9px;color:#fff;font-size:26px;font-weight:500;letter-spacing:-.3px}
.brand-dot{width:16px;height:16px;border-radius:50%;background:#fff}
.badge{position:absolute;left:139px;top:82px;width:136px;height:136px;border-radius:50%;background:#fff;box-shadow:0 6px 18px rgba(0,0,0,.12)}
.tabs{position:absolute;left:25px;top:246px;white-space:nowrap;font-size:14.5px;color:var(--ink)}
.tab{position:absolute;top:0}
.tab--on{color:var(--teal);font-weight:700}
.tab-underline{position:absolute;height:3px;background:var(--teal)}
.rule{position:absolute;height:1px;background:var(--line)}
.pill-bar{position:absolute;left:27px;width:360px;height:46px;border-radius:23px;background:var(--grad);color:#fff;font-weight:700;font-size:15px;display:flex;align-items:center;justify-content:center;gap:12px;letter-spacing:.2px}
.pill-bar--left{justify-content:flex-start;padding-left:22px}
.pill-bar .q{position:absolute;right:20px;top:15px}
.card{position:absolute;left:26px;width:362px;height:196px}
.card .row{position:absolute;left:0;font-size:14.5px;white-space:nowrap}
.card .lbl{font-weight:700;color:var(--ink);letter-spacing:.2px}
.card .val{position:absolute;left:107px;top:0;color:var(--muted);font-size:15px;font-weight:400}
.card .name{color:var(--muted);font-size:15px}
.ok{color:var(--green)!important}
.bad{color:var(--red)!important}
.card-sep{position:absolute;left:0;top:158px;width:362px;height:1px;background:#d9d9d9}
.photo{position:absolute;left:263px;top:-3px;width:96px;height:96px;border-radius:50%;border:3px solid #fff;box-shadow:0 4px 14px rgba(0,0,0,.2)}
.dim{position:absolute;left:0;top:0;width:414px;height:240px;background:rgba(12,10,24,.82)}
.sheet{position:absolute;left:0;top:119px;width:414px;height:1300px;background:#fff;border-radius:40px 40px 0 0}
.handle{position:absolute;left:173px;top:22px;width:68px;height:5px;border-radius:3px;background:var(--teal)}
.outline-btn{position:absolute;left:27px;width:360px;height:48px;border-radius:24px;border:1.5px solid transparent;
  background:linear-gradient(#fff,#fff) padding-box,var(--grad) border-box;
  box-shadow:0 6px 16px rgba(42,168,208,.15);color:var(--teal);font-weight:700;font-size:15px;display:flex;align-items:center;justify-content:center;gap:14px}
.section-title{position:absolute;left:25px;color:var(--teal);font-weight:700;font-size:13.5px;letter-spacing:.2px}
.field{position:absolute;left:27px;width:360px;height:46px;border-radius:23px;border:1px solid #e3edf5;box-shadow:0 4px 14px rgba(42,168,208,.10);
  display:flex;align-items:center;padding-left:21px;font-size:15px;color:var(--muted);gap:16px;white-space:nowrap}
.field b{color:var(--purple);font-weight:700;letter-spacing:.2px}
.field--tall{height:140px;border-radius:22px;display:block;padding:14px 21px;white-space:normal}
.field--tall p{margin-top:12px;line-height:26px;font-size:14.5px;white-space:normal;overflow-wrap:break-word}
.comments{position:absolute;left:27px;top:847px;width:360px;height:178px;border-radius:20px;background:var(--grad);color:#fff;padding:14px 22px}
.comments b{font-size:15px;letter-spacing:.2px}
.comments p{font-size:15px;margin-top:10px}
.chip{position:absolute;top:118px;height:37px;border-radius:19px;background:#fff;color:var(--teal);font-weight:700;font-size:13.5px;display:flex;align-items:center;justify-content:center;gap:8px}
.solid-btn{position:absolute;height:36px;border-radius:18px;color:#fff;font-size:15px;display:flex;align-items:center;justify-content:center;gap:9px}
.solid-btn--teal{background:var(--teal)}
.solid-btn--purple{background:var(--purple)}
.plain{position:absolute;left:26px;font-size:15px;color:var(--muted)}
.plain b{color:#000;font-weight:700}
</style>
</head>
<body>
<div class="stage">

  <svg width="0" height="0" style="position:absolute">
    <defs>
      <linearGradient id="hdr" x1="0" y1="0" x2="1" y2="0">
        <stop offset="0" stop-color="#2aa8d0"/><stop offset=".5" stop-color="#3b8fc8"/><stop offset="1" stop-color="#6a4fa3"/>
      </linearGradient>
    </defs>
  </svg>

  <section class="screen screen--list">
    <svg class="header" viewBox="0 0 414 240"><path d="M0 0H414V95Q300 160 207 160Q110 160 0 98Z" fill="url(#hdr)"/></svg>
    <div class="icon-btn" style="left:27px"><svg width="18" height="18" viewBox="0 0 18 18" fill="#3b8fc8"><rect x="1" y="1" width="7" height="7" rx="2"/><rect x="10" y="1" width="7" height="7" rx="2"/><rect x="1" y="10" width="7" height="7" rx="2"/><rect x="10" y="10" width="7" height="7" rx="2"/></svg></div>
    <div class="brand"><span class="brand-dot"></span>ShiftCover</div>
    <div class="icon-btn" style="left:297px"><svg width="18" height="18" viewBox="0 0 18 18" fill="none" stroke="#3b8fc8" stroke-width="1.8"><circle cx="8" cy="8" r="5.5"/><path d="M12 12l4 4"/></svg></div>
    <div class="icon-btn" style="left:347px"><svg width="16" height="18" viewBox="0 0 16 18" fill="#5a6bb5"><circle cx="8" cy="5" r="4"/><path d="M0 18c0-5 3.5-7 8-7s8 2 8 7z"/></svg></div>
    <div class="badge"></div>

    <div class="tabs">
      <span class="tab tab--on" style="left:0">MY ASSIGNMENTS</span>
      <span class="tab" style="left:153px">AVAILABLE OPENINGS</span>
      <span class="tab" style="left:327px">MY ASSIGNMENTS</span>
    </div>
    <div class="tab-underline" style="left:25px;top:274px;width:128px"></div>

    <div class="pill-bar pill-bar--left" style="top:301px">
      <svg width="14" height="15" viewBox="0 0 14 15" fill="#fff"><path d="M3 0h11v11H4a1.5 1.5 0 000 3h10v1H3.5A3 3 0 010 12V3a3 3 0 013-3z"/></svg>
      MY ASSIGNMENTS
      <svg class="q" width="14" height="14" viewBox="0 0 14 14"><circle cx="7" cy="7" r="7" fill="#fff"/><text x="7" y="11" font-size="10" font-weight="700" text-anchor="middle" fill="#6a4fa3" font-family="Arial">?</text></svg>
    </div>

    <article class="card" style="top:372px">
      <div class="row lbl" style="top:0">SUBBING FOR:</div>
      <div class="row name" style="top:27px">Nora Hale, (Teacher) <svg width="14" height="14" viewBox="0 0 14 14" style="vertical-align:-2px;margin-left:4px"><circle cx="7" cy="7" r="7" fill="#4a9a2e"/><path d="M3.8 7.2l2.2 2.2 4.2-4.4" stroke="#fff" stroke-width="1.8" fill="none"/></svg></div>
      <div class="row lbl" style="top:58px">LOCATION:<span class="val">PRES</span></div>
      <div class="row lbl" style="top:88px">STATUS:<span class="val ok">Complete</span></div>
      <div class="row lbl" style="top:118px">TIME SLOTS:<span class="val">09/02 – 09/02 (1h 0m)</span></div>
      <div class="photo" role="img" aria-label="Portrait photo of the teacher being covered" style="background:radial-gradient(circle at 50% 40%,#c99a7a 0%,#6b4a34 45%,#1f5a48 100%)"></div>
      <div class="card-sep"></div>
    </article>

    <article class="card" style="top:568px">
      <div class="row lbl" style="top:0">SUBBING FOR:</div>
      <div class="row name" style="top:27px">Extra duty (Teacher)</div>
      <div class="row lbl" style="top:58px">LOCATION:<span class="val">PRES</span></div>
      <div class="row lbl" style="top:88px">STATUS:<span class="val ok">Complete</span></div>
      <div class="row lbl" style="top:118px">TIME SLOTS:<span class="val">07/10 – 07/11 (1h 20m)</span></div>
      <div class="card-sep"></div>
    </article>

    <article class="card" style="top:763px">
      <div class="row lbl" style="top:0">SUBBING FOR:</div>
      <div class="row name" style="top:27px">Owen Price (Administrator) <svg width="14" height="14" viewBox="0 0 14 14" style="vertical-align:-2px;margin-left:4px"><circle cx="7" cy="7" r="7" fill="#4a9a2e"/><path d="M3.8 7.2l2.2 2.2 4.2-4.4" stroke="#fff" stroke-width="1.8" fill="none"/></svg></div>
      <div class="row lbl" style="top:58px">LOCATION:<span class="val">PRES</span></div>
      <div class="row lbl" style="top:88px">STATUS:<span class="val ok">Active</span></div>
      <div class="row lbl" style="top:118px">TIME SLOTS:<span class="val">07/26 – 08/07 (14h 15m)</span></div>
      <div class="photo" role="img" aria-label="Portrait photo of the administrator being covered" style="background:radial-gradient(circle at 50% 40%,#c98c6a 0%,#f2b48a 55%,#1c2233 100%)"></div>
      <div class="card-sep"></div>
    </article>

    <article class="card" style="top:959px">
      <div class="row lbl" style="top:0">SUBBING FOR:</div>
      <div class="row name" style="top:27px">Lena Ortiz (Teacher) <svg width="14" height="14" viewBox="0 0 14 14" style="vertical-align:-2px;margin-left:4px"><circle cx="7" cy="7" r="7" fill="#4a9a2e"/><path d="M3.8 7.2l2.2 2.2 4.2-4.4" stroke="#fff" stroke-width="1.8" fill="none"/></svg></div>
      <div class="row lbl" style="top:58px">LOCATION:<span class="val">PRES</span></div>
      <div class="row lbl" style="top:88px">STATUS:<span class="val bad">Canceled</span></div>
      <div class="row lbl" style="top:118px">TIME SLOTS:<span class="val">07/31 – 07/31 (9h 0m)</span></div>
      <div class="photo" role="img" aria-label="Portrait photo of the teacher being covered" style="background:radial-gradient(circle at 50% 35%,#9a6a4c 0%,#d9c4b4 45%,#f4f2f0 100%)"></div>
      <div class="card-sep"></div>
    </article>

    <article class="card" style="top:1154px">
      <div class="row lbl" style="top:0">SUBBING FOR:</div>
      <div class="row name" style="top:27px">Caleb Reyes (Teacher) <svg width="14" height="14" viewBox="0 0 14 14" style="vertical-align:-2px;margin-left:4px"><circle cx="7" cy="7" r="7" fill="#4a9a2e"/><path d="M3.8 7.2l2.2 2.2 4.2-4.4" stroke="#fff" stroke-width="1.8" fill="none"/></svg></div>
      <div class="row lbl" style="top:58px">LOCATION:<span class="val">PRES</span></div>
      <div class="row lbl" style="top:88px">STATUS:<span class="val ok">Active</span></div>
      <div class="row lbl" style="top:118px">TIME SLOTS:<span class="val">07/31 – 07/31 (9h 0m)</span></div>
      <div class="photo" role="img" aria-label="Portrait photo of the teacher being covered" style="background:radial-gradient(circle at 50% 35%,#b98365 0%,#e3d6cf 50%,#8fb3d6 100%)"></div>
    </article>
  </section>

  <section class="screen screen--menu">
    <svg class="header" viewBox="0 0 414 240"><path d="M0 0H414V95Q300 160 207 160Q110 160 0 98Z" fill="url(#hdr)"/></svg>
    <div class="icon-btn" style="left:27px"></div>
    <div class="brand"><span class="brand-dot"></span>ShiftCover</div>
    <div class="icon-btn" style="left:297px"></div>
    <div class="icon-btn" style="left:347px"></div>
    <div class="badge"></div>
    <div class="dim"></div>

    <div class="sheet">
      <div class="handle"></div>
      <div class="pill-bar" style="top:56px">
        <svg width="15" height="13" viewBox="0 0 15 13" fill="#fff"><path d="M7.5 0L15 6.5h-2V13H9V9H6v4H2V6.5H0z"/></svg>HOME</div>
      <div class="pill-bar" style="top:119px">
        <svg width="14" height="14" viewBox="0 0 14 14" fill="none" stroke="#fff" stroke-width="2"><circle cx="7" cy="7" r="5.5"/><path d="M7 4v3.5H4.5"/></svg>AVAILABLE OPENINGS</div>
      <div class="pill-bar" style="top:182px">
        <svg width="14" height="15" viewBox="0 0 14 15" fill="#fff"><path d="M3 0h11v11H4a1.5 1.5 0 000 3h10v1H3.5A3 3 0 010 12V3a3 3 0 013-3z"/></svg>ASSIGNMENTS</div>
      <div class="pill-bar" style="top:245px">
        <svg width="14" height="14" viewBox="0 0 14 14"><circle cx="7" cy="7" r="7" fill="#fff"/><text x="7" y="11" font-size="10" font-weight="700" text-anchor="middle" fill="#3b8fc8" font-family="Arial">?</text></svg>SUPPORT</div>

      <div class="outline-btn" style="top:367px">
        <svg width="17" height="14" viewBox="0 0 17 14" fill="#2aa8d0"><path d="M5 0h7l1.5 2H17v12H0V2h3.5z"/><circle cx="8.5" cy="8" r="3.2" fill="#fff"/></svg>NO PROFILE IMAGE CLICK HERE</div>
      <div class="outline-btn" style="top:434px">
        <svg width="13" height="15" viewBox="0 0 16 18" fill="#2aa8d0"><circle cx="8" cy="5" r="4"/><path d="M0 18c0-5 3.5-7 8-7s8 2 8 7z"/></svg>USER ACCOUNT</div>
      <div class="outline-btn" style="top:500px">
        <svg width="16" height="16" viewBox="0 0 16 16" fill="none" stroke="#2aa8d0" stroke-width="2"><path d="M12 9v5H2V4h5M9 1h6v6M15 1L7 9"/></svg>LOGOUT</div>
    </div>
  </section>

  <section class="screen screen--detail">
    <svg class="header" viewBox="0 0 414 240"><path d="M0 0H414V95Q300 160 207 160Q110 160 0 98Z" fill="url(#hdr)"/></svg>
    <div class="icon-btn" style="left:27px"><svg width="18" height="18" viewBox="0 0 18 18" fill="#3b8fc8"><rect x="1" y="1" width="7" height="7" rx="2"/><rect x="10" y="1" width="7" height="7" rx="2"/><rect x="1" y="10" width="7" height="7" rx="2"/><rect x="10" y="10" width="7" height="7" rx="2"/></svg></div>
    <div class="brand"><span class="brand-dot"></span>ShiftCover</div>
    <div class="icon-btn" style="left:297px"><svg width="18" height="18" viewBox="0 0 18 18" fill="none" stroke="#3b8fc8" stroke-width="1.8"><circle cx="8" cy="8" r="5.5"/><path d="M12 12l4 4"/></svg></div>
    <div class="icon-btn" style="left:347px"><svg width="16" height="18" viewBox="0 0 16 18" fill="#5a6bb5"><circle cx="8" cy="5" r="4"/><path d="M0 18c0-5 3.5-7 8-7s8 2 8 7z"/></svg></div>
    <div class="badge"></div>

    <div class="section-title" style="top:247px">OPENING INFORMATION</div>
    <div class="rule" style="left:25px;top:276px;width:389px"></div>
    <div class="tab-underline" style="left:25px;top:274px;width:198px"></div>

    <div class="field" style="top:304px"><b>SUMMARY:</b>Testing-test</div>
    <div class="field" style="top:368px"><b>LOCATION:</b>Pine Ridge Elementary School</div>
    <div class="field" style="top:431px"><b>TYPE:</b>Vacancy</div>
    <div class="field" style="top:495px"><b>REGULAR STAFF:</b>Miles Carter</div>
    <div class="field" style="top:559px"><b>ASSIGNMENT CATEGORY:</b>Teacher</div>
    <div class="field" style="top:622px"><b>DEPARTMENT:</b></div>
    <div class="field field--tall" style="top:686px"><b>DESCRIPTION:</b>
      <p>Ut enim ad minima veniam, quis nostrum exer citationem ullam corporis suscipit labori osam, nisi ut aliquid ex ea commodi consequatur?</p></div>

    <div class="comments">
      <b>COMMENTS:</b>
      <p>Write a comment or upload a file...</p>
      <div class="chip" style="left:22px;width:94px">
        <svg width="15" height="13" viewBox="0 0 15 13" fill="#2aa8d0"><path d="M0 0h6l6 6-6 6-6-6z"/><path d="M8 0h2l5 6-5 6H9l5-6z"/></svg>POST</div>
      <div class="chip" style="left:127px;width:114px">
        <svg width="13" height="13" viewBox="0 0 13 13" fill="#2aa8d0"><path d="M6.5 0L11 5H8v4H5V5H2z"/><rect x="0" y="10" width="13" height="3"/></svg>UPLOAD</div>
    </div>

    <div class="field" style="top:1043px;gap:12px">
      <svg width="16" height="13" viewBox="0 0 16 13" fill="#555"><ellipse cx="6" cy="5" rx="6" ry="4.5"/><ellipse cx="11" cy="8.5" rx="5" ry="4"/></svg>No comments or files uploaded</div>

    <div class="section-title" style="top:1125px">ADDITIONAL DETAILS</div>
    <div class="rule" style="left:25px;top:1157px;width:389px"></div>
    <div class="tab-underline" style="left:25px;top:1155px;width:158px"></div>

    <div class="field" style="top:1184px"><b>PARKING SPOT:</b></div>

    <div class="plain" style="top:1256px;color:#000;font-weight:700;font-size:15.5px">TIME SLOTS</div>
    <div class="solid-btn solid-btn--teal" style="left:27px;top:1292px;width:110px">
      <svg width="13" height="13" viewBox="0 0 14 14"><circle cx="7" cy="7" r="7" fill="#fff"/><path d="M3.8 7.2l2.2 2.2 4.2-4.4" stroke="#2aa8d0" stroke-width="1.8" fill="none"/></svg>Accept</div>
    <div class="solid-btn solid-btn--purple" style="left:147px;top:1292px;width:120px">
      <svg width="13" height="13" viewBox="0 0 14 14"><circle cx="7" cy="7" r="7" fill="#fff"/><rect x="3.5" y="6" width="7" height="2" fill="#6a4fa3"/></svg>Withdraw</div>

    <div class="field" style="top:1351px"><b style="display:flex;gap:12px;align-items:center"><svg width="14" height="14" viewBox="0 0 14 14" fill="#6a4fa3"><rect x="0" y="2" width="14" height="12" rx="1"/><rect x="3" y="0" width="2" height="4"/><rect x="9" y="0" width="2" height="4"/><rect x="2" y="6" width="10" height="6" fill="#fff"/></svg>DATE:</b>03/09/2024</div>
    <div class="field" style="top:1417px;width:180px;gap:14px"><b style="display:flex;gap:12px;align-items:center"><svg width="14" height="14" viewBox="0 0 14 14" fill="#6a4fa3"><rect x="0" y="2" width="14" height="12" rx="1"/><rect x="3" y="0" width="2" height="4"/><rect x="9" y="0" width="2" height="4"/><rect x="2" y="6" width="10" height="6" fill="#fff"/></svg>FROM:</b>9.30 AM</div>
    <div class="field" style="top:1417px;left:223px;width:164px;gap:8px"><b style="display:flex;gap:12px;align-items:center"><svg width="14" height="14" viewBox="0 0 14 14" fill="#6a4fa3"><rect x="0" y="2" width="14" height="12" rx="1"/><rect x="3" y="0" width="2" height="4"/><rect x="9" y="0" width="2" height="4"/><rect x="2" y="6" width="10" height="6" fill="#fff"/></svg>TO:</b>12.30 PM</div>

    <div class="plain" style="top:1491px"><b>CURRENT ASSIGNMENT:</b> No Assignment</div>
    <div class="plain" style="top:1519px"><b>STATUS:</b> Active</div>

    <div class="solid-btn solid-btn--teal" style="left:174px;top:1565px;width:100px">
      <svg width="13" height="13" viewBox="0 0 14 14"><circle cx="7" cy="7" r="7" fill="#fff"/><path d="M3.8 7.2l2.2 2.2 4.2-4.4" stroke="#2aa8d0" stroke-width="1.8" fill="none"/></svg>Save</div>
    <div class="solid-btn solid-btn--purple" style="left:287px;top:1565px;width:100px">
      <svg width="13" height="13" viewBox="0 0 14 14"><circle cx="7" cy="7" r="7" fill="#fff"/><rect x="3.5" y="6" width="7" height="2" fill="#6a4fa3"/></svg>Close</div>
  </section>

</div>
</body>
</html>
```